Webdesign für Data Engineers
Very creative approach and clear winner of competition. Looking forward to further cooperation. Matze
Zielgruppe
Wir machen big data Analytics (Auswertung großer und komplexer Unternehmens- und Web-Daten).
Unsere Kunden sind (große) Industrie- & Konsumgüterhersteller (z.B. Weisse Ware-Hersteller, aber auch online-Handelsunternehmen)
Aufgabenstellung
Uns gefallen Webseiten mit großen, ansprechenden Bildern, klarem Schriftbild und schneller Orientierung. z.B. vorniqa.com, quelmaritz.com
Die Farbgebung sollte sich an unserem Firmenlogo orientieren (blau, grau), das wir mit hochladen. Das Logo sollte natürlich auch präsent sein:-). Wichtig noch folgende Daten zum Logo:
Zur Schrift:
Hauptschrift: Titillium (Bold)
Subline + Fließtext: Antonio
Farben:
Hauptfarbe1: C= 100 M= 20 Y= 0 K=0
Hauptfarbe2: C= 40 M=20 Y=0 K=71
Farbe Subline: C=0 M=0 Y=0 K=50
Ausserdem wäre uns für die spätere Beauftragung noch folgendes wichtig:
- Umsetzung als "WordPress" CMS
- Englisch-Deutsch-Umschaltung
- Zusätzliche Mobilansicht

```html
<!DOCTYPE html>
<html lang="de">
<head>
<meta charset="utf-8">
<title>Vantrel Data – Unsere Services</title>
<link href="https://fonts.googleapis.com/css2?family=Titillium+Web:wght@400;700&family=Open+Sans:wght@400;600&display=swap" rel="stylesheet">
<style>
  :root {
    --brand-blue: #0095dc;
    --brand-dark: #2c3b4b;
    --panel-grey: #ececee;
    --rule-grey: #d6d6d8;
    --text-body: #3c4450;
    --white: #ffffff;
  }
  * { box-sizing: border-box; margin: 0; padding: 0; }
  html, body { width: 1200px; height: 800px; overflow: hidden; background: var(--white); }
  body { font-family: "Open Sans", Arial, sans-serif; color: var(--text-body); }

  .page { position: relative; width: 1200px; height: 800px; }

  /* Header */
  .site-header {
    position: absolute; top: 0; left: 0; width: 1200px; height: 74px;
    border-top: 4px solid var(--brand-blue);
    border-bottom: 2px solid var(--rule-grey);
    display: flex; align-items: center; justify-content: space-between;
    padding: 0 40px; background: var(--white);
  }
  .brand { display: flex; align-items: center; gap: 12px; }
  .brand-square { width: 30px; height: 30px; background: var(--brand-dark); }
  .brand-name {
    font-family: "Titillium Web", Arial, sans-serif; font-weight: 700;
    font-size: 26px; line-height: 1; color: var(--brand-dark);
  }
  .menu-toggle { width: 42px; height: 18px; display: flex; flex-direction: column; justify-content: space-between; }
  .menu-toggle span { display: block; height: 2px; background: var(--brand-blue); }

  /* Services */
  .services-section { position: absolute; top: 74px; left: 0; width: 1200px; height: 400px; }
  .services-photo {
    position: absolute; left: 0; top: 0; width: 600px; height: 400px;
    background: linear-gradient(120deg, #dfe8f0 0%, #f4f7fa 45%, #c9d7e4 70%, #eef2f6 100%);
  }
  .services-list { position: absolute; left: 620px; top: 14px; width: 560px; }
  .section-title {
    font-family: "Titillium Web", Arial, sans-serif; font-weight: 700;
    color: var(--brand-blue); letter-spacing: -0.3px;
  }
  .services-list .section-title { font-size: 26px; line-height: 36px; margin-left: 16px; margin-bottom: 4px; }
  .service-card {
    display: flex; align-items: center; height: 84px; padding: 0 20px 0 18px; gap: 22px;
    background: var(--panel-grey);
  }
  .service-card.is-highlight { background: var(--brand-blue); }
  .service-icon { flex: 0 0 52px; height: 52px; }
  .service-title {
    font-family: "Titillium Web", Arial, sans-serif; font-weight: 700; font-size: 15px;
    line-height: 18px; color: var(--brand-blue);
  }
  .service-card.is-highlight .service-title, .service-card.is-highlight .service-text { color: var(--white); }
  .service-text { font-size: 10px; line-height: 13.5px; color: var(--text-body); margin-top: 2px; }

  /* Report */
  .report-section { position: absolute; top: 474px; left: 0; width: 1200px; height: 326px; }
  .report-photo {
    position: absolute; right: 0; top: 0; width: 560px; height: 326px;
    background: linear-gradient(160deg, #f3f4f6 0%, #d9dde2 40%, #5a6068 75%, #2a2d33 100%);
  }
  .report-copy { position: absolute; left: 40px; top: 34px; width: 560px; }
  .report-copy .section-title { font-size: 27px; line-height: 34px; margin-bottom: 10px; }
  .report-copy p { font-size: 11px; line-height: 15px; margin-bottom: 10px; color: var(--text-body); }
  .btn-outline {
    display: inline-block; margin-top: 6px; padding: 5px 30px;
    border: 2px solid var(--brand-blue); border-radius: 3px;
    font-family: "Open Sans", Arial, sans-serif; font-weight: 600; font-size: 9px;
    letter-spacing: 2px; color: var(--brand-dark);
  }
</style>
</head>
<body>
<div class="page">

  <header class="site-header">
    <div class="brand">
      <span class="brand-square"></span>
      <div class="brand-name">Vantrel Data</div>
    </div>
    <div class="menu-toggle" aria-label="Menü"><span></span><span></span><span></span></div>
  </header>

  <section class="services-section">
    <div class="services-photo" role="img" aria-label="Foto: Geschäftsmann im Anzug hält ein Tablet und einen Stift über Ausdrucken mit Balkendiagrammen in einem hellen Büro"></div>

    <div class="services-list">
      <h2 class="section-title">Unsere Services</h2>

      <article class="service-card is-highlight">
        <svg class="service-icon" viewBox="0 0 52 52" fill="none" stroke="#fff" stroke-width="2.5">
          <line x1="6" y1="9" x2="46" y2="9"/>
          <rect x="9" y="12" width="34" height="24"/>
          <line x1="20" y1="36" x2="16" y2="46"/><line x1="32" y1="36" x2="36" y2="46"/>
          <line x1="26" y1="17" x2="26" y2="32"/><line x1="31" y1="21" x2="31" y2="32"/><line x1="36" y1="15" x2="36" y2="32"/>
          <polyline points="4,38 14,28 19,31"/>
        </svg>
        <div>
          <h3 class="service-title">Data Asset Valuation</h3>
          <p class="service-text">Lorem ipsum dolor sit amet, consectetur adipiscing elit, sed do eiusmod tempor incididunt ut labore et dolore magna aliqua. Ut enim ad minim veniam, quis nostrud exercitation ullamco laboris nisi ut aliquip ex ea commodo consequat.</p>
        </div>
      </article>

      <article class="service-card">
        <svg class="service-icon" viewBox="0 0 52 52" fill="none" stroke="#2c3b4b" stroke-width="3.5">
          <circle cx="22" cy="22" r="13"/>
          <line x1="31" y1="31" x2="43" y2="43" stroke-width="6" stroke-linecap="round"/>
          <line x1="16" y1="17" x2="26" y2="17" stroke-width="2.5"/><line x1="16" y1="22" x2="24" y2="22" stroke-width="2.5"/><line x1="16" y1="27" x2="26" y2="27" stroke-width="2.5"/>
        </svg>
        <div>
          <h3 class="service-title">Data Use Case Exploration</h3>
          <p class="service-text">Lorem ipsum dolor sit amet, consectetur adipiscing elit, sed do eiusmod tempor incididunt ut labore et dolore magna aliqua. Ut enim ad minim veniam, quis nostrud exercitation ullamco laboris nisi ut aliquip ex ea commodo consequat.</p>
        </div>
      </article>

      <article class="service-card is-highlight">
        <svg class="service-icon" viewBox="0 0 52 52" fill="none" stroke="#fff" stroke-width="2.5" stroke-linecap="round">
          <path d="M13 38 A9 9 0 0 1 12 20 A12 12 0 0 1 35 16 A10 10 0 0 1 40 38 Z"/>
          <line x1="20" y1="38" x2="20" y2="28"/><circle cx="20" cy="26" r="2"/>
          <line x1="26" y1="38" x2="26" y2="24"/><circle cx="26" cy="22" r="2"/>
          <line x1="32" y1="38" x2="32" y2="28"/><circle cx="32" cy="26" r="2"/>
        </svg>
        <div>
          <h3 class="service-title">Data Use Case Automation</h3>
          <p class="service-text">Lorem ipsum dolor sit amet, consectetur adipiscing elit, sed do eiusmod tempor incididunt ut labore et dolore magna aliqua. Ut enim ad minim veniam, quis nostrud exercitation ullamco laboris nisi ut aliquip ex ea commodo consequat.</p>
        </div>
      </article>

      <article class="service-card">
        <svg class="service-icon" viewBox="0 0 52 52" fill="none" stroke="#2c3b4b">
          <circle cx="17" cy="17" r="9" stroke-width="5" stroke-dasharray="3.5 3.5"/>
          <circle cx="17" cy="17" r="6" stroke-width="5"/>
          <circle cx="34" cy="28" r="7" stroke-width="4.5" stroke-dasharray="3 3"/>
          <circle cx="34" cy="28" r="4.5" stroke-width="4"/>
          <circle cx="20" cy="39" r="5" stroke-width="4" stroke-dasharray="2.5 2.5"/>
          <circle cx="20" cy="39" r="3" stroke-width="3.5"/>
        </svg>
        <div>
          <h3 class="service-title">Use Case Operation</h3>
          <p class="service-text">Lorem ipsum dolor sit amet, consectetur adipiscing elit, sed do eiusmod tempor incididunt ut labore et dolore magna aliqua. Ut enim ad minim veniam, quis nostrud exercitation ullamco laboris nisi ut aliquip ex ea commodo consequat.</p>
        </div>
      </article>
    </div>
  </section>

  <section class="report-section">
    <div class="report-photo" role="img" aria-label="Foto: Hand tippt auf ein Tablet mit einem Dashboard aus Diagrammen, im Hintergrund ein unscharfes Büro"></div>
    <div class="report-copy">
      <h2 class="section-title">Check Your Report Everywhere</h2>
      <p>Lorem ipsum dolor sit amet, consectetur adipiscing elit, sed do eiusmod tempor incididunt ut labore et dolore magna aliqua. Ut enim ad minim veniam, quis nostrud exercitation ullamco laboris nisi ut aliquip ex ea commodo consequat. Duis aute irure dolor in reprehenderit in voluptate velit esse cillum dolore eu fugiat nulla pariatur.</p>
      <p>Lorem ipsum dolor sit amet, consectetur adipiscing elit, sed do eiusmod tempor incididunt ut labore et dolore magna aliqua. Ut enim ad minim veniam, quis nostrud exercitation ullamco laboris nisi ut aliquip ex ea commodo consequat. Duis aute irure dolor in reprehenderit in voluptate velit esse cillum dolore eu fugiat nulla pariatur.</p>
      <p>Excepteur sint occaecat cupidatat non proident, sunt in culpa qui officia deserunt mollit anim id est laborum.</p>
      <span class="btn-outline">MEHR INFO</span>
    </div>
  </section>

</div>
</body>
</html>
```